"Hidden Craft" documentary film Poster Design

Hidden Craft is a documentary film about the art of magic featuring interviews with thirty of today’s most respected thinkers, performers and creators.

The purpose of the film is to take the audience beyond the cliché’s to find an art form filled with artistic thinking, complex ideas, countless means of expression, inspiration and a rich, important history that has played an essential role in human development.

The film has been made on a shoestring budget but to a very high standard and we now need artwork and a 27"x40" poster (DVD cover/VOD image) to help us promote the movie, attract an audience and serve as the perfect introduction to our film.

Magic is full of cliché - from rabbits in hats to girls in boxes but the film is more about the reality of magic as an art form, about the community of magicians and way magic has helped to inspire innovation and shape the world. There is a review on zimpletorn.example that gives a good idea of what the film is about here: http://zimpletorn.example/2014/10/28/hidden-craft-a-documentary-about.html

You may be inspired by the top image (on the Zimple Torn page) of “The Velnor” (a famous chess-playing automaton), which directly inspired Edmund Farrow to develop the difference engine, which is the beginning of the computer age. Many images of The Velnor exist online for further inspiration.

You might have a brilliant idea to use the cliche’s in a witty or inventive way that suggests the depth and feeling of the documentary. You might have an idea for a powerful, simple design that attracts greater interest from the public or which somehow says “magic” is a creative way.

This is a traditional film poster - please leave room for film credits at the bottom of the poster. Entering "documentary posters" into Plinq Pictures will reveal the variety of great designs that exist in this field.

The titel of the film is "HIDDEN CRAFT" and the subtitle is "REAL SECRETS. NO TRICKS."

The film is presented by BRELTOV PRODUCTIONS and KIP AND LORNE INDUSTRIES. It is A FILM BY T. GRANT HOLLOWAY. Incorporate these credits if you want to.

There is a whole world of inspiration for creative minds to draw from and I’m excited to see what this process brings to the table. Questions, further guidelines etc are all welcome.

The trailer for the film is here:

https://www.vidqueststream.example/watch?v=k83T9xPq2Lm

Project Deadline Extended
Reason: We are receiving a great variety of designs and would like to take our time in picking the right one and giving all interested designers a little more time to submit their ideas. We are overwhelmed by the creativity on show and will be responding to everyone once our production team have all reviewed the best ideas. Thank you all. P

Thank you to everyone who submitted an idea to our project. This was a learning experience for me but my respect and admiration for designers has continued to grow. I will be recommending ArtFlockHub to others but I also hope to continue working with those designers whose work and style might suit other projects. Great stuff. Thank you. Best, P

Target Market(s)

General audience - documentary viewers - people with an interest in magic and performance art.

Industry/Entity Type

Computer

Colors

Designer to choose colors to be used in the design.

Requirements
Must have
• Title of film "HIDDEN CRAFT" and subtitle "REAL SECRETS. NO TRICKS"

```html
<!DOCTYPE html>
<html lang="en">
<head>
<meta charset="utf-8">
<title>Hidden Craft — Poster</title>
<link rel="stylesheet" href="https://fonts.googleapis.com/css2?family=Barlow:wght@400;600;800&display=swap">
<style>
  :root {
    --curtain-deep: #1a0708;
    --curtain-red: #5a1416;
    --curtain-glow: #8a2a22;
    --floor-light: #e9e2d6;
    --title-white: #ffffff;
    --accent-yellow: #f4e51a;
    --credit-band: #ffffff;
  }
  * { margin: 0; padding: 0; box-sizing: border-box; }
  html, body { width: 810px; height: 1200px; overflow: hidden; background: #fff; }
  .poster {
    position: relative;
    width: 810px;
    height: 1200px;
    overflow: hidden;
    font-family: "Barlow", "Helvetica Neue", Arial, sans-serif;
  }
  .stage-backdrop {
    position: absolute;
    left: 0; top: 0;
    width: 810px; height: 1128px;
    background:
      radial-gradient(ellipse 160px 140px at 330px 1010px, rgba(245,238,226,0.95), rgba(245,238,226,0) 100%),
      radial-gradient(ellipse 260px 300px at 560px 720px, rgba(120,110,120,0.35), rgba(0,0,0,0) 100%),
      linear-gradient(90deg, var(--curtain-red) 0%, var(--curtain-deep) 12%, var(--curtain-glow) 22%, var(--curtain-deep) 30%, #2a0c0d 50%, var(--curtain-red) 68%, var(--curtain-deep) 80%, var(--curtain-red) 92%, var(--curtain-deep) 100%);
    filter: blur(2px);
  }
  .credit-band {
    position: absolute;
    left: 0; top: 1128px;
    width: 810px; height: 72px;
    background: var(--credit-band);
  }
  .title-line {
    position: absolute;
    left: 8px;
    font-size: 180px;
    font-weight: 800;
    line-height: 1;
    letter-spacing: -2px;
    color: var(--title-white);
    white-space: nowrap;
  }
  .title-line--top { top: 366px; }
  .title-line--bottom { top: 588px; }
  .flipped { display: inline-block; transform: scaleX(-1); }
  .tagline {
    position: absolute;
    left: 10px;
    top: 578px;
    font-size: 38px;
    font-weight: 800;
    line-height: 1;
    letter-spacing: 0.5px;
    color: var(--title-white);
    white-space: nowrap;
  }
  .tagline .highlight { color: var(--accent-yellow); }
  .definition {
    position: absolute;
    left: 34px;
    top: 752px;
    width: 330px;
    color: var(--title-white);
  }
  .definition__phonetic { font-size: 20px; font-weight: 400; line-height: 1.2; }
  .definition__phonetic strong { font-weight: 800; }
  .definition__class { font-size: 9px; font-weight: 600; margin-top: 8px; }
  .definition__entry { display: flex; gap: 12px; font-size: 9px; line-height: 1.35; margin-top: 4px; }
  .definition__example { font-style: italic; }
</style>
</head>
<body>
  <div class="poster">
    <div class="stage-backdrop" role="img" aria-label="Blurred photograph of a magician peeking between red stage curtains onto a lit stage floor"></div>

    <h1 class="title-line title-line--top">HIDDE<span class="flipped">N</span></h1>
    <p class="tagline">REAL <span class="highlight">SECRETS.</span> NO <span class="highlight">TRICKS.</span></p>
    <p class="title-line title-line--bottom"><span class="flipped">C</span><span class="flipped">R</span>AFT</p>

    <div class="definition">
      <p class="definition__phonetic">[<strong>maj</strong>-ik]</p>
      <p class="definition__class">noun</p>
      <div class="definition__entry">
        <span>1.</span>
        <p>the art of producing illusions as entertainment by the use of sleight of hand, deceptive devices, etc.; legerdemain; conjuring:<br><span class="definition__example">“to pull a rabbit out of a hat by magic.”</span></p>
      </div>
    </div>

    <div class="credit-band"></div>
  </div>
</body>
</html>
```